依頼詳細
発泡スチロール製品の事例を紹介するリーフレットのデザインをお願い致します。
発泡スチロールの箱をいろいろな業種の方にご利用いただいております。いろいろな発泡スチロールの利用状況とお客様の声を今後DMとして発送を計画しております。
シリーズとして使えるようにしていきたいと考えております。今回は緑系統で、今後は色を替えることも想定してデザインをお願いできればと思います。
記載項目
社名、電話番号、ホームページアドレス、所在地
サイズ
A4
ページ数
片面
希望イメージ
シンプル 複雑
単色 カラフル
暗い 明るい
日常 高級
遊び心 厳粛
未来的 伝統的
女性的 男性的
希望する色
緑系、ロゴの色
納品ファイル
• イラストレーター形式 (.ai)
補足説明
ロゴデータはありません。添付書類参照下さい。
お世話になっております。コンペ参加者の皆様大変申し訳ありませんが、もう少し提案数が必要なため提案期日を10日延長いたしました。
現在参加されている方には大変申し訳ありませんがご理解いただきますようお願い申し上げます。
■ 選んだ理由

大変素晴らしいデザインありがとうございました。
お客様も大変悩まれておりましたが、大変気に入って頂けました。

■ 提案者全員のお礼・コメント

沢山のご提案ありがとうございました。
今後共デザインコンペを行ってまいりますのでよろしくお願いいたします。

```html
<!DOCTYPE html>
<html lang="ja">
<head>
<meta charset="utf-8">
<title>販売事例 No.01 アイス保冷用発泡スチロール</title>
<link href="https://fonts.googleapis.com/css2?family=Noto+Sans+JP:wght@400;500;700;900&display=swap" rel="stylesheet">
<style>
  :root{
    --green-deep:#1e3328;
    --green-line:#3d5a46;
    --gold:#c9a961;
    --gold-soft:#e2cf9c;
    --paper:#ffffff;
    --ink:#1d2b22;
    --brand:#2e7d3a;
    --muted:#d9e2db;
  }
  *{box-sizing:border-box;margin:0;padding:0}
  html,body{width:848px;height:1200px;overflow:hidden;background:#e9ece9}
  body{font-family:"Noto Sans JP",sans-serif;color:var(--muted)}
  .leaflet{position:relative;width:848px;height:1200px;background:var(--green-deep);overflow:hidden}

  .header{padding:30px 48px 16px;border-bottom:1px solid var(--green-line)}
  .case-no{font-size:15px;font-weight:700;color:var(--gold-soft);letter-spacing:.05em}
  .title{margin-top:4px;font-size:44px;font-weight:900;color:var(--paper);letter-spacing:.04em;line-height:1.2}

  .block{display:flex;padding:26px 48px 24px 40px}
  .side-label{writing-mode:vertical-rl;font-size:15px;font-weight:700;color:var(--paper);letter-spacing:.25em;padding-right:22px;border-right:1px solid var(--green-line);margin-right:26px}
  .requests{list-style:none;flex:1;display:flex;flex-direction:column;gap:22px}
  .request{display:flex;gap:18px;align-items:flex-start}
  .req-mark{flex:0 0 44px;text-align:center}
  .req-tag{display:block;font-size:9px;border:1px solid var(--gold);color:var(--gold);padding:1px 0;border-radius:2px}
  .req-num{display:block;font-size:34px;font-weight:700;color:var(--paper);line-height:1.05}
  .req-text{font-size:12.5px;line-height:1.8;color:var(--muted);padding-top:4px}

  .proposal{padding:20px 48px 0}
  .section-head{display:flex;align-items:center;gap:16px;color:var(--gold-soft);font-size:19px;font-weight:700;letter-spacing:.08em}
  .section-head::before,.section-head::after{content:"";flex:1;height:1px;background:var(--gold)}
  .proposal-text{margin-top:14px;font-size:12px;line-height:1.8}
  .photos{display:flex;gap:18px;margin-top:16px}
  .photo{height:200px;border-radius:2px}
  .photo-a{flex:1.25;background:linear-gradient(135deg,#2b2a25,#5a4a32 55%,#b9a27a)}
  .photo-b{flex:1;background:linear-gradient(160deg,#f1efe8,#d9d3c3 60%,#8f7b55)}

  .voice{padding-top:30px}
  .voice-text{font-size:12.5px;line-height:1.85;flex:1}
  .voice-text strong{color:var(--paper);font-weight:700}

  .footer{position:absolute;left:0;right:0;bottom:0;height:215px;background:var(--paper);color:var(--ink);padding:16px 48px}
  .contact-row{display:flex;align-items:center;gap:18px;border-bottom:2px solid var(--brand);padding-bottom:8px}
  .contact-label{font-size:15px;font-weight:700}
  .phone{display:flex;align-items:center;gap:10px;font-size:44px;font-weight:900;color:var(--brand);letter-spacing:.02em;line-height:1.2}
  .company{display:flex;align-items:flex-start;gap:18px;margin-top:14px}
  .brand{display:flex;flex-direction:column;align-items:center;gap:6px;width:104px}
  .brand-square{width:56px;height:56px;background:var(--brand)}
  .brand-name{font-size:12px;font-weight:700;color:var(--brand);letter-spacing:.05em}
  .company-info{flex:1}
  .tagline{font-size:14px;font-weight:700}
  .company-name{font-size:28px;font-weight:900;line-height:1.3}
  .address{font-size:12px;margin-top:2px}
  .company-extra{text-align:right;padding-top:24px}
  .fax{font-size:21px;font-weight:700}
  .url{font-size:19px;font-weight:700;margin-top:6px}
</style>
</head>
<body>
<main class="leaflet">
  <header class="header">
    <p class="case-no">【販売事例 No.01】</p>
    <h1 class="title">アイス保冷用発泡スチロール</h1>
  </header>

  <section class="block requests-block">
    <h2 class="side-label">お客様からのご要望</h2>
    <ol class="requests">
      <li class="request"><div class="req-mark"><span class="req-tag">要望</span><span class="req-num">1</span></div>
        <p class="req-text">新商品のアイスクリームを開発中で、そのアイスクリームは生乳や生クリームなど素材にこだわった<br>今までに無い高級なアイスクリームを販売したい。</p></li>
      <li class="request"><div class="req-mark"><span class="req-tag">要望</span><span class="req-num">2</span></div>
        <p class="req-text">名前は「翠雪アイス」で3個入りの発泡スチロール容器が必要だが、<br>保冷性能が高く外観も高級感を持ったパッケージにしたい。</p></li>
      <li class="request"><div class="req-mark"><span class="req-tag">要望</span><span class="req-num">3</span></div>
        <p class="req-text">販売数量は特別なものではないが、型代などの経費はかけたくない。</p></li>
    </ol>
  </section>

  <section class="proposal">
    <h2 class="section-head">ミドリパックからのご提案</h2>
    <p class="proposal-text">嗜好性・付加価値を高めた結果、下記のように既存品をベースにパッケージのご提案をしました。<br>「要望1」については今回は当社既製品カップを使い高級感のある製品を提案し、「要望2」の外観については高級感を出せるカラーのブランド製品を提案。</p>
    <div class="photos">
      <div class="photo photo-a" role="img" aria-label="3個入り発泡スチロールカップを収めた高級感のある箱の写真"></div>
      <div class="photo photo-b" role="img" aria-label="ブランドカラーの箱と発泡スチロールカップを並べた写真"></div>
    </div>
  </section>

  <section class="block voice">
    <h2 class="side-label">お客様からの声</h2>
    <p class="voice-text">「発泡スチロール容器が自由では他には無い」との考えがあり、提出したサンプルが「翠雪アイス」のコンセプトに合致していた。<br>理由としては発泡スチロール容器のブランド色が重厚感や本格の味わいを感じさせることと、中仕切りは高色でブランド色とマッチして高級感が感じられ「翠雪アイス」のこだわりを表現したことが決め手となった。<br>また本数量の事業であり「今回の採用は、<strong>ミドリパックからの総合的な提案力が決め手となった</strong>」とのお言葉も頂きました。</p>
  </section>

  <footer class="footer">
    <div class="contact-row">
      <span class="contact-label">お問い合わせは</span>
      <span class="phone">
        <svg width="36" height="36" viewBox="0 0 24 24" aria-hidden="true"><path fill="#2e7d3a" d="M6.6 10.8a15 15 0 0 0 6.6 6.6l2.2-2.2c.3-.3.7-.4 1-.2 1.1.4 2.3.6 3.6.6.6 0 1 .4 1 1V20c0 .6-.4 1-1 1A17 17 0 0 1 3 4c0-.6.4-1 1-1h3.5c.6 0 1 .4 1 1 0 1.3.2 2.5.6 3.6.1.3 0 .7-.2 1z"/></svg>
        0299-10-4821
      </span>
    </div>
    <div class="company">
      <div class="brand">
        <span class="brand-square"></span>
        <span class="brand-name">MIDORIPACK</span>
      </div>
      <div class="company-info">
        <p class="tagline">最高品質は必ずミドリパックで見つかる</p>
        <p class="company-name">株式会社ミドリパック</p>
        <p class="address">〒100-0000 架空県緑野市森町2番地</p>
      </div>
      <div class="company-extra">
        <p class="fax">FAX. 0299-10-4822</p>
        <p class="url">www.midoripack-sample.jp</p>
      </div>
    </div>
  </footer>
</main>
</body>
</html>
```